Email signature and business card

Australian company called Tarrowin. We provide construction and maintenance services to the mining industry. I would like the design to be similar to our website theme(www.tarrowin.com.au) whilst staying compact. RGB colours to include: 42,96,140 and 232,163,0 and I have attached 2 logos.

The following fields will need to be included:

Full Name
Title
Location/Project
Phone
Mobile
Fax
Email
Web site

Target Market(s)

Mining Industry

Industry/Entity Type

Construction

Requirements
Must have
• Full Name, Title, Office Address, Phone, Mobile, Fax, Email, Web address
• Back of card must include: Boilermaking, Carpentry, Concrete, Construction, Cranes, Data and Comms, Electrical, Fabrication, Fitting, Labour Hire, Plumbing, Rigging, Shutdowns

```html
<!DOCTYPE html>
<html lang="en">
<head>
<meta charset="utf-8">
<title>Tarrowin Business Card</title>
<link href="https://fonts.googleapis.com/css2?family=Open+Sans:wght@400;600;700&display=swap" rel="stylesheet">
<style>
  :root {
    --brand-blue: rgb(42, 96, 140);
    --brand-blue-dark: #1c4a70;
    --brand-blue-light: #3d8fbd;
    --brand-yellow: rgb(232, 163, 0);
    --brand-yellow-bright: #f2c318;
    --ink: #3a3a3a;
    --muted: #7a7a7a;
    --paper: #ffffff;
    --backdrop: #e9e6e1;
  }
  * { box-sizing: border-box; margin: 0; padding: 0; }
  html, body { width: 1200px; height: 1023px; overflow: hidden; }
  body {
    background: var(--backdrop);
    font-family: "Open Sans", Arial, sans-serif;
    position: relative;
  }
  .card {
    position: absolute;
    left: 230px;
    width: 740px;
    height: 452px;
    border-radius: 6px;
    overflow: hidden;
    box-shadow: 0 10px 30px rgba(0,0,0,0.18);
  }
  /* Front */
  .card-front { top: 40px; background: var(--paper); }
  .front-base {
    position: absolute; left: 0; right: 0; bottom: 0; height: 18px;
    background: var(--brand-blue-light);
  }
  .icon-tab {
    position: absolute; left: 0; bottom: 0; width: 150px; height: 52px;
    background: var(--brand-blue-light);
    border-top-right-radius: 18px;
    display: flex; align-items: center; justify-content: center; gap: 14px;
  }
  .icon-tab svg { width: 20px; height: 20px; }
  .wordmark { position: absolute; left: 44px; top: 48px; display: flex; align-items: center; gap: 14px; }
  .wordmark-dot { width: 44px; height: 44px; border-radius: 50%; background: var(--brand-blue); }
  .wordmark-name {
    font-weight: 600; font-size: 40px; color: var(--brand-blue); line-height: 1;
  }
  .badges { position: absolute; right: 40px; top: 28px; display: flex; gap: 8px; }
  .badge { width: 78px; height: 86px; border: 2px solid var(--brand-blue); background: #eef3f8; }
  .badge-dark { background: var(--brand-blue); }
  .top-rule {
    position: absolute; left: 400px; right: 40px; top: 128px; height: 2px;
    background: linear-gradient(to right, transparent, var(--brand-blue-light));
  }
  .person { position: absolute; left: 44px; top: 176px; }
  .person-name { font-size: 26px; font-weight: 700; color: var(--brand-blue-light); letter-spacing: 0.5px; }
  .person-title { font-size: 14px; color: var(--muted); letter-spacing: 1px; margin-top: 2px; }
  .name-rule {
    position: absolute; left: 44px; top: 250px; width: 380px; height: 2px;
    background: linear-gradient(to right, var(--brand-blue-light), transparent);
  }
  .contact { position: absolute; left: 150px; top: 282px; font-size: 19px; color: var(--ink); line-height: 32px; }
  .office { position: absolute; left: 440px; top: 176px; font-size: 19px; color: var(--ink); line-height: 32px; }
  .office-label { color: var(--brand-yellow); font-weight: 600; }
  .office-line { display: flex; align-items: center; gap: 10px; }
  .office-line svg { width: 18px; height: 18px; }
  /* Back */
  .card-back {
    top: 531px;
    background: linear-gradient(160deg, var(--brand-blue-light) 0%, var(--brand-blue) 55%, var(--brand-blue-dark) 100%);
  }
  .back-decoration {
    position: absolute; right: 0; bottom: 0; width: 320px; height: 300px;
    background: radial-gradient(ellipse at 70% 70%, rgba(255,255,255,0.10), rgba(255,255,255,0) 70%);
  }
  .back-wordmark {
    position: absolute; left: 60px; top: 64px;
    font-weight: 600; font-size: 72px; color: var(--brand-yellow-bright); line-height: 1;
  }
  .services { position: absolute; left: 60px; top: 236px; display: flex; gap: 70px; }
  .service-list { list-style: none; font-size: 19px; color: #fff; line-height: 34px; }
  .service-list li::before {
    content: ""; display: inline-block; width: 8px; height: 8px; border-radius: 50%;
    background: var(--brand-yellow-bright); margin-right: 10px; vertical-align: middle;
  }
</style>
</head>
<body>
  <section class="card card-front">
    <div class="wordmark">
      <span class="wordmark-dot"></span>
      <span class="wordmark-name">Tarrowin</span>
    </div>
    <div class="badges">
      <span class="badge"></span>
      <span class="badge badge-dark"></span>
    </div>
    <div class="top-rule"></div>

    <div class="person">
      <div class="person-name">CALUM FERRIER</div>
      <div class="person-title">DIRECTOR</div>
    </div>
    <div class="name-rule"></div>

    <div class="contact">
      <div>0412 738 590</div>
      <div>calum@tarrowin.com.au</div>
      <div>www.tarrowin.com.au</div>
    </div>

    <div class="office">
      <div class="office-label">Head Office</div>
      <div>Level 3, 14 Harbour Drive</div>
      <div>Mooloolaba QLD 4557</div>
      <div class="office-line">
        <svg viewBox="0 0 20 20"><path d="M4 3h4l2 5-2.5 1.5a11 11 0 0 0 3 3L12 10l5 2v4a2 2 0 0 1-2 2A14 14 0 0 1 2 5a2 2 0 0 1 2-2z" fill="var(--brand-yellow)"/></svg>
        <span>(07) 5520 3140</span>
      </div>
      <div class="office-line">
        <svg viewBox="0 0 20 20"><rect x="5" y="2" width="10" height="6" fill="var(--brand-yellow)"/><rect x="2" y="8" width="16" height="8" rx="2" fill="var(--brand-yellow)"/><rect x="5" y="13" width="10" height="5" fill="#fff" stroke="var(--brand-yellow)"/></svg>
        <span>(07) 5520 3188</span>
      </div>
    </div>

    <div class="front-base"></div>
    <div class="icon-tab">
      <svg viewBox="0 0 20 20"><rect x="5" y="1" width="10" height="18" rx="2" fill="var(--brand-yellow-bright)"/></svg>
      <svg viewBox="0 0 20 20"><rect x="1" y="4" width="18" height="12" fill="var(--brand-yellow-bright)"/><path d="M1 4l9 7 9-7" stroke="var(--brand-blue-light)" fill="none" stroke-width="1.5"/></svg>
      <svg viewBox="0 0 20 20"><circle cx="10" cy="10" r="8.5" fill="var(--brand-yellow-bright)"/><path d="M1.5 10h17M10 1.5v17M4 5h12M4 15h12" stroke="var(--brand-blue-light)" stroke-width="1.2" fill="none"/></svg>
    </div>
  </section>

  <section class="card card-back">
    <div class="back-decoration" role="img" aria-label="Faint brand illustration area"></div>
    <div class="back-wordmark">Tarrowin</div>
    <div class="services">
      <ul class="service-list">
        <li>Boilermaking</li><li>Carpentry</li><li>Concrete</li><li>Construction</li><li>Cranes</li>
      </ul>
      <ul class="service-list">
        <li>Data and Comms</li><li>Electrical</li><li>Fabrication</li><li>Fitting</li>
      </ul>
      <ul class="service-list">
        <li>Labour Hire</li><li>Plumbing</li><li>Rigging</li><li>Shutdowns</li>
      </ul>
    </div>
  </section>
</body>
</html>
```